Web Design for Real Estate Lending business

I need a web design for my real estate private lending business. The name of the business is Halvern Capital Group. I plan on using Wordpress because that platform is the most optimized for SEO, and we will rely heavily on SEO after the website is built.

I want the website to be responsive of course, and have a fresh, professional, and sleek UI.

The 4 main goals of the website will be:
1. Rank in Google for our relevant key words (Los Angeles real estate hard money lending, real estate financing, fix and flip, private lending, etc)
2. Educate them on what our lending platform is capable of.
3. Capture the contact info (email or phone number) of investors & borrowers who are interested
4. Encourage investors and borrowers to contact us directly

This is an example of a similar business's website: https://www.morvelcapital.example/

Here is my business parter's old website:
https://web.archive.org/web/20180822043430/http://www.dumaleqg.example/

All of the information on that website (2nd link) will apply to our business. You can pull the information from that Dumale QG website and make it look more modern / sleek, similar to the 1st link (but better).

We are not selling anything on the website.

I also attached a business card template. I would like something similar to this but one that looks slightly more corporate / professional. Keep the colors the same though.

```html
<!DOCTYPE html>
<html lang="en">
<head>
<meta charset="utf-8">
<title>Halvern Capital Group – Hard Money Lenders</title>
<link href="https://fonts.googleapis.com/css2?family=Montserrat:wght@400;500;600;700&family=Didact+Gothic&display=swap" rel="stylesheet">
<style>
:root{
  --navy:#173a69;
  --navy-deep:#0f2d56;
  --blue:#0b58b8;
  --blue-text:#1759b0;
  --ink:#1e1e1e;
  --muted:#444;
  --line:#c9ced6;
  --soft:#f3f3f3;
  --white:#fff;
}
*{box-sizing:border-box;margin:0;padding:0}
html,body{width:1200px;height:4766px;overflow:hidden}
body{position:relative;font-family:"Montserrat",sans-serif;color:var(--ink);background:var(--white)}
.abs{position:absolute}
.display{font-family:"Didact Gothic",sans-serif}
/* hero */
.hero{left:0;top:0;width:1200px;height:660px;background:linear-gradient(180deg,#8fb2d6 0%,#b6c9d8 28%,#98a7a6 45%,#6f8f5e 70%,#4f7c3a 100%)}
.brand{left:30px;top:28px;display:flex;align-items:center;gap:12px}
.brand-mark{width:50px;height:50px;background:var(--navy)}
.brand-name{font-weight:700;font-size:23px;line-height:26px;color:var(--navy);text-transform:uppercase;letter-spacing:.3px}
.main-nav{left:496px;top:74px;display:flex;gap:28px;font-size:12.5px;text-transform:uppercase;color:#1d2a3b}
.main-nav .active{font-weight:600}
.search{left:956px;top:24px}
.btn-financing{left:998px;top:20px;width:152px;height:38px;background:var(--blue);color:#fff;border-radius:3px;font-size:17px;display:flex;align-items:center;justify-content:center}
.hero-title{left:68px;top:222px;font-size:82px;font-weight:700;color:#124a8f;letter-spacing:1px;font-family:"Montserrat",sans-serif}
.hero-tag{left:70px;width:368px;height:28px;background:#1f1f1f;color:#fff;font-size:24px;line-height:28px;padding-left:12px}
/* tabs */
.tabs{left:148px;top:673px;width:906px;height:56px;background:var(--blue);border-radius:6px;display:flex;align-items:center;justify-content:center;gap:16px;color:#fff;font-size:17px}
.tabs .active{font-weight:700}
.tabs .sep{opacity:.8}
.intro-title{left:0;top:758px;width:1200px;text-align:center;font-size:29px;letter-spacing:.4px}
.intro-text{left:130px;width:940px;text-align:center;font-size:13.5px;line-height:23px;color:var(--muted)}
/* collateral band */
.collateral{left:0;top:984px;width:1200px;height:324px;background:var(--navy)}
.collateral h2{position:absolute;left:0;top:52px;width:1200px;text-align:center;color:#fff;font-size:29px;font-weight:600;letter-spacing:.5px}
.types{position:absolute;left:30px;top:150px;width:1140px;display:flex;justify-content:space-between}
.type{width:114px;text-align:center;color:#fff;font-size:13.5px;line-height:20px}
.type svg{display:block;margin:0 auto 12px}
/* transactions */
.photo{border-radius:12px}
.section-h{font-size:32px;font-weight:500}
.section-h span{color:var(--blue-text)}
.date{font-size:15px;text-decoration:underline}
.body-text{font-size:14px;line-height:22px;color:var(--muted)}
.btn-small{background:var(--blue);color:#fff;border-radius:3px;font-size:14px;display:flex;align-items:center;justify-content:center}
.btn-outline{left:716px;top:1874px;width:374px;height:61px;border:2px solid var(--blue);border-radius:4px;color:var(--blue);font-size:22px;display:flex;align-items:center;justify-content:center;letter-spacing:.5px}
/* rates */
.rates{left:0;top:2025px;width:1200px;height:824px;background:var(--soft)}
.rate{width:226px;height:70px;border-radius:6px;background:#fff;border:1px solid #dde1e6;box-shadow:0 3px 8px rgba(0,0,0,.12);text-align:center;padding-top:10px}
.rate b{display:block;font-size:23px;font-weight:600}
.rate small{font-size:12px;color:#555}
.rate.on{background:var(--blue);color:#fff;border-color:var(--blue)}
.rate.on small{color:#e8eef8}
/* info cards */
.call{left:0;top:2885px;width:1200px;text-align:center;font-size:29px;line-height:45px}
.call .link{color:var(--blue-text)}
.card{width:350px;height:511px;border:1.5px solid #555;border-top:none;background:#fff}
.card .pic{position:absolute;left:6px;top:0;width:336px;height:296px}
.card h3{position:absolute;left:18px;top:318px;font-size:16px;font-weight:600}
.card p{position:absolute;left:18px;top:352px;width:312px;font-size:14px;line-height:22px;text-align:justify;color:#333}
.card .tag{position:absolute;right:-1px;bottom:-1px;height:32px;padding:0 14px;background:var(--blue);color:#fff;font-size:11.5px;font-weight:600;display:flex;align-items:center}
/* cash band */
.cash{left:0;top:3543px;width:1200px;height:283px;background:linear-gradient(90deg,#20426f,#2b5588 50%,#20426f)}
.cash h2{position:absolute;top:44px;width:1200px;text-align:center;color:#fff;font-size:46px;font-weight:700}
.cash p{position:absolute;top:112px;width:1200px;text-align:center;color:#fff;font-size:18px;line-height:30px}
.cash .go{position:absolute;left:507px;top:205px;width:189px;height:43px;border:2px solid #fff;color:#fff;font-size:22px;font-weight:600;display:flex;align-items:center;justify-content:center}
/* form */
.form-title{left:146px;top:3855px;font-size:42px;font-weight:500}
.form-note{left:573px;top:3876px;font-size:14px}
.field{height:65px;border:1.5px solid #b5bcc6;font-size:14px;color:#888;padding:0 31px;display:flex;align-items:center}
.question{left:0;top:4219px;width:1200px;text-align:center;font-size:15px}
.check{display:flex;align-items:center;gap:16px;font-size:15px}
.check i{width:20px;height:20px;border:1.5px solid #2d6dc1;display:block}
.btn-submit{left:503px;top:4333px;width:196px;height:48px;background:var(--blue);border-radius:4px;color:#fff;font-size:27px;letter-spacing:1px;display:flex;align-items:center;justify-content:center}
/* footer */
.foot{left:0;top:4412px;width:1200px;height:246px;background:#f4f4f4}
.foot h4{position:absolute;top:26px;font-size:24px;font-weight:500;letter-spacing:.5px}
.foot p{position:absolute;font-size:12px;line-height:22px;color:#333}
.foot ul{position:absolute;list-style:none;font-size:12px;line-height:28px;color:#333}
.foot li:before{content:"› ";color:#777}
.base{left:0;top:4658px;width:1200px;height:108px;background:var(--navy-deep);color:#fff}
.base h5{position:absolute;left:66px;top:34px;font-size:30px;font-weight:600}
.base .row{position:absolute;display:flex;align-items:center;gap:8px;font-size:16px}
.social{position:absolute;top:28px;width:54px;height:54px;border:2px solid #fff;border-radius:50%}
</style>
</head>
<body>

<!-- Hero -->
<div class="abs hero" role="img" aria-label="Aerial view of a city skyline with green parkland"></div>
<div class="abs brand"><div class="brand-mark"></div><div class="brand-name">Halvern<br>Capital Group</div></div>
<svg class="abs search" width="26" height="26" viewBox="0 0 26 26"><circle cx="11" cy="11" r="8" fill="none" stroke="#1d2a3b" stroke-width="2"/><line x1="17" y1="17" x2="24" y2="24" stroke="#1d2a3b" stroke-width="2"/></svg>
<div class="abs btn-financing">Get financing</div>
<nav class="abs main-nav"><span class="active">Hard Money</span><span>Debt Consolidaton</span><span>Bridge Loans</span><span>Fix &amp; Flip</span><span>Ask a Private Lender</span></nav>
<h1 class="abs hero-title">Hard Money Lenders</h1>
<div class="abs hero-tag" style="top:338px">No Hassle Process</div>
<div class="abs hero-tag" style="top:380px">We work with all credit</div>
<div class="abs hero-tag" style="top:422px">Quick Qualify</div>
<div class="abs hero-tag" style="top:464px">We'll get you what you need</div>

<!-- Tabs & intro -->
<div class="abs tabs"><span class="active">Loan Options</span><span class="sep">|</span><span>Property Values</span><span class="sep">|</span><span>Property Types</span><span class="sep">|</span><span>Investors</span><span class="sep">|</span><span>Recommended Professionals</span></div>
<h2 class="abs intro-title display">Dumale Capital Group – Your Fast and Reliable Hard Money Specialists</h2>
<p class="abs intro-text" style="top:813px;left:220px;width:760px">Do you need hard money in a hurry to purchase investment property,build your dream home or quick cash? When banks say no, Dumale Capital Group says YES!</p>
<p class="abs intro-text" style="top:880px">Welcome to Dumale Capital Group. With more than 100 years combined experience our trained professionals have the knowledge and expertise to customize a loan specific to your needs. We are a private lender. We have the ability to fund in a fraction of the time of traditional banks and lenders. Take the frustration out of borrowing money and call your funding source today</p>

<!-- Collateral types -->
<section class="abs collateral">
  <h2>Some Types of Real Estate/Property to Serve as Collateral Include:</h2>
  <div class="types">
    <div class="type"><svg width="70" height="70" viewBox="0 0 70 70" fill="none" stroke="#fff" stroke-width="2"><rect x="14" y="10" width="30" height="56"/><rect x="44" y="28" width="14" height="38"/><path d="M20 18h6M32 18h6M20 28h6M32 28h6M20 38h6M32 38h6M20 48h6M32 48h6M48 36h6M48 46h6"/></svg>Office<br>Buildings</div>
    <div class="type"><svg width="70" height="70" viewBox="0 0 70 70" fill="none" stroke="#fff" stroke-width="2"><path d="M14 66V16l16-8v58M30 66V24l20 6v36"/><path d="M19 24h6M19 34h6M19 44h6M36 38h8M36 48h8"/></svg>Multi-Family<br>Apartments</div>
    <div class="type"><svg width="70" height="70" viewBox="0 0 70 70" fill="none" stroke="#fff" stroke-width="2"><path d="M10 66V30l14 10V30l14 10V30l14 10V12h8v54z"/><path d="M18 54h6M32 54h6M46 54h6"/></svg>Industrial<br>Properties</div>
    <div class="type"><svg width="70" height="70" viewBox="0 0 70 70" fill="none" stroke="#fff" stroke-width="2"><path d="M6 36L35 10l29 26M14 30v36h42V30"/><circle cx="30" cy="42" r="3"/><path d="M30 46v10M40 44v12"/></svg>Assisted<br>Living Condos</div>
    <div class="type"><svg width="70" height="70" viewBox="0 0 70 70" fill="none" stroke="#fff" stroke-width="2"><path d="M10 26l6-14h38l6 14zM10 26c0 5 10 5 10 0 0 5 10 5 10 0 0 5 10 5 10 0 0 5 10 5 10 0 0 5 10 5 10 0M14 32v34h42V32"/><rect x="22" y="42" width="12" height="24"/><rect x="40" y="42" width="10" height="10"/></svg>Retail<br>Centers</div>
    <div class="type"><svg width="70" height="70" viewBox="0 0 70 70" fill="none" stroke="#fff" stroke-width="2"><path d="M14 52a21 21 0 0 1 42 0zM8 58h54M35 25v-5M31 20h8"/></svg>Hospitality<br>Properties</div>
    <div class="type"><svg width="70" height="70" viewBox="0 0 70 70" fill="none" stroke="#fff" stroke-width="2"><path d="M8 30L35 12l27 18v36H8z"/><rect x="20" y="36" width="30" height="30"/><path d="M20 44h30M20 52h30M20 60h30"/></svg>Self<br>Storages</div>
    <div class="type"><svg width="70" height="70" viewBox="0 0 70 70" fill="none" stroke="#fff" stroke-width="2"><rect x="18" y="12" width="34" height="54"/><path d="M24 20h6M40 20h6M24 30h6M40 30h6M24 40h6M40 40h6M30 66V54h10v12"/></svg>Condo<br>Units</div>
    <div class="type"><svg width="70" height="70" viewBox="0 0 70 70" fill="none" stroke="#fff" stroke-width="2"><rect x="22" y="8" width="26" height="58" rx="3"/><rect x="27" y="16" width="16" height="14"/><path d="M28 38h4M38 38h4M28 46h4M38 46h4M28 54h4M38 54h4"/></svg>Mobile<br>Home Parks</div>
    <div class="type"><svg width="70" height="70" viewBox="0 0 70 70" fill="none" stroke="#fff" stroke-width="2"><circle cx="35" cy="36" r="27"/><circle cx="23" cy="36" r="3.5"/><circle cx="35" cy="36" r="3.5"/><circle cx="47" cy="36" r="3.5"/></svg>And<br>More</div>
  </div>
</section>

<!-- Transactions -->
<div class="abs photo" style="left:326px;top:1356px;width:392px;height:285px;background:linear-gradient(180deg,#c8d2dc,#7b8896 60%,#4c5560)" role="img" aria-label="Downtown street with glass skyscrapers"></div>
<div class="abs photo" style="left:30px;top:1500px;width:272px;height:309px;background:linear-gradient(180deg,#b9c9da,#8b6f62 55%,#4e4640)" role="img" aria-label="Busy avenue lined with brick high-rises"></div>
<div class="abs photo" style="left:326px;top:1667px;width:299px;height:287px;background:linear-gradient(180deg,#2b3340,#4c5666 60%,#a78a5a)" role="img" aria-label="Twin towers lit up at night"></div>
<h2 class="abs section-h display" style="left:772px;top:1430px">What is <span>Lorem Ipsum?</span></h2>
<div class="abs date" style="left:772px;top:1500px">May 2020</div>
<p class="abs body-text" style="left:772px;top:1540px;width:390px">Lorem Ipsum is simply dummy text of the printing and typesetting industry. Lorem Ipsum has been the industry's standard dummy text ever since the 1500s, when an unknown</p>
<p class="abs body-text" style="left:772px;top:1654px;width:390px">Lorem Ipsum is simply dummy text of the printing and typesetting industry.</p>
<div class="abs btn-small" style="left:1019px;top:1735px;width:137px;height:37px">Read More...</div>
<div class="abs btn-outline">SEE MORE TRANSACTIONS</div>

<!-- Rates -->
<section class="abs rates"></section>
<div class="abs" style="left:55px;top:2055px;width:445px;height:751px;background:linear-gradient(160deg,#e9e2d6,#cfc6b8 50%,#8b8f96)" role="img" aria-label="Person reviewing a financial chart with a calculator"></div>
<h2 class="abs section-h display" style="left:532px;top:2102px;font-size:30px">What is <span>Lorem Ipsum?</span></h2>
<p class="abs body-text" style="left:532px;top:2186px;width:620px;font-size:13.5px">Lorem Ipsum is simply dummy text of the printing and typesetting industry. Lorem Ipsum has been the industry's standard dummy .</p>
<div class="abs rate" style="left:582px;top:2323px"><b>Fees</b><small>As low as 2%</small></div>
<div class="abs rate on" style="left:582px;top:2421px"><b>Fees</b><small>As low as 2%</small></div>
<div class="abs rate" style="left:582px;top:2519px"><b>Fees</b><small>As low as 2%</small></div>
<div class="abs rate" style="left:582px;top:2617px"><b>Fees</b><small>As low as 2%</small></div>
<div class="abs rate on" style="left:878px;top:2323px"><b>Loan Amounts</b><small>$500,000 - $100,000,000</small></div>
<div class="abs rate" style="left:878px;top:2421px"><b>Loan Amounts</b><small>$500,000 - $100,000,000</small></div>
<div class="abs rate" style="left:878px;top:2519px"><b>Loan Amounts</b><small>$500,000 - $100,000,000</small></div>
<div class="abs rate on" style="left:878px;top:2617px"><b>Loan Amounts</b><small>$500,000 - $100,000,000</small></div>

<!-- Info cards -->
<div class="abs call display">For More Information please call us at (555) 014-2287!!<br><span class="link">or <b style="font-family:Montserrat,sans-serif;font-weight:600">Click Here to Apply Now!</b></span></div>
<div class="abs card" style="left:61px;top:2997px"><div class="pic" style="background:linear-gradient(160deg,#eef0f2,#d6d9dc 60%,#b9b5a8)" role="img" aria-label="Hands fanning out a stack of dollar bills"></div><h3>Bills Piling Up?</h3><p>With Dumale Capital Group, you'll be back on top of your mountain of paperwork instead of buried underneath it! Let the experienced team members here help consolidate your debt.</p><span class="tag">Debt Consolidation</span></div>
<div class="abs card" style="left:431px;top:2997px"><div class="pic" style="background:linear-gradient(160deg,#dcdcdc,#9a9a9a 60%,#4a4a4a)" role="img" aria-label="Builder in a hard hat and plaid shirt"></div><h3>Finance Your Project</h3><p>Building a new property? Expanding an operation? Not sure what kind of funding you need? Dumale Capital Group will help you get the funds you need to get the project done!</p><span class="tag">Ask A Private Lender</span></div>
<div class="abs card" style="left:801px;top:2997px"><div class="pic" style="background:linear-gradient(160deg,#d9dde0,#8f7560 55%,#4b3a2e)" role="img" aria-label="Team meeting around a wooden table with laptops"></div><h3>Recommended Professionals</h3><p>These are individuals and companies that Dumale Capital Group works with and trust to provide you with the same level of service you have come to expect here over the years.</p><span class="tag">See who is recommended!</span></div>

<!-- Get Cash -->
<section class="abs cash" role="img" aria-label="Blue tinted background of banknotes">
  <h2 class="display" style="font-family:Montserrat,sans-serif">Get Cash Now!</h2>
  <p>Use this form to receive FREE advice from one of the experienced professionals here regarding any<br>Private Money Loan related topics. It's quick, it's easy, and the more questions you answer – the more accurate your results.</p>
  <div class="go">GET STARTED!</div>
</section>

<!-- Stay informed -->
<h2 class="abs form-title">Stay Informed</h2>
<div class="abs form-note">To receive email alerts</div>
<div class="abs field" style="left:107px;top:3935px;width:940px">Email</div>
<div class="abs field" style="left:107px;top:4027px;width:441px">First Name</div>
<div class="abs field" style="left:609px;top:4027px;width:438px">Last Name</div>
<div class="abs field" style="left:107px;top:4116px;width:441px">Company</div>
<div class="abs field" style="left:609px;top:4116px;width:438px">Job Title</div>
<p class="abs question">What information are you most interested in? <b>(Select all that apply)</b></p>
<div class="abs check" style="left:395px;top:4267px"><i></i>Investor Newsletter</div>
<div class="abs check" style="left:605px;top:4267px"><i></i>Borrower Newsletter</div>
<div class="abs btn-submit">SUBMIT</div>

<!-- Footer -->
<footer class="abs foot">
  <h4 style="left:102px">ABOUT HALVERN</h4>
  <p style="left:76px;top:70px;width:290px">Lorem Ipsum is simply dummy text of the printing and typesetting industry. Lorem Ipsum has been the industry's standard dummy .</p>
  <div class="btn-small" style="position:absolute;left:145px;top:192px;width:130px;height:30px;font-size:11.5px;font-weight:600">Check Availability</div>
  <h4 style="left:472px">NAVIGATION</h4>
  <ul style="left:418px;top:64px"><li>Home</li><li>About</li><li>Glossary</li><li>Checklists</li><li>Property Values</li></ul>
  <ul style="left:596px;top:64px"><li>Property Types</li><li>Local Resources</li><li>Recommended Professionals</li><li>Privacy Policy</li><li>Terms of Use</li></ul>
  <h4 style="left:882px">LATEST NEWS</h4>
  <p style="left:846px;top:70px;width:290px">Lorem Ipsum is simply dummy text of the printing and typesetting industry. Lorem Ipsum has been the industry's standard dummy .</p>
  <div style="position:absolute;left:1041px;top:190px;width:129px;height:33px;border:1.5px solid #333;border-radius:3px;font-size:11.5px;font-weight:600;display:flex;align-items:center;justify-content:center">Read More</div>
</footer>
<div class="abs base">
  <h5 class="display">Contact</h5>
  <div class="row" style="left:250px;top:18px"><svg width="18" height="18" viewBox="0 0 18 18" fill="none" stroke="#fff" stroke-width="1.5"><circle cx="9" cy="9" r="8"/><path d="M6 5l2 2-1 1.5a6 6 0 0 0 2.5 2.5L11 10l2 2-1 1.5C9 13 5 9 4.5 6z"/></svg>(555) 014-2287
    <svg width="22" height="16" viewBox="0 0 22 16" fill="none" stroke="#fff" stroke-width="1.5" style="margin-left:10px"><rect x="1" y="1" width="20" height="14"/><path d="M1 1l10 8 10-8"/></svg>jnorell@dumaleqg.example</div>
  <div class="row" style="left:220px;top:56px"><svg width="18" height="22" viewBox="0 0 18 22" fill="none" stroke="#fff" stroke-width="1.5"><path d="M9 21s-7-7-7-12a7 7 0 0 1 14 0c0 5-7 12-7 12z"/><circle cx="9" cy="9" r="2.5"/></svg>418 Harbor Crest Dr &nbsp;Bayview, CA. 90210</div>
  <div class="social" style="left:857px"></div>
  <div class="social" style="left:946px"></div>
  <div class="social" style="left:1035px"></div>
</div>

</body>
</html>
```